Floor Inspections and Consulting

We provide inspections and consulting services on various floor coverings, e.g. carpet, hardwood, etc. We also do expert witness work for attorneys due to floor covering failures. We current have a logo, just need it incorporated into a new design. I have examples of cards I have found on the internet that capture my attention and make a statement. I have included our original business card, which in my opinion is terrible, but it does have our logo on it.

```html
<!DOCTYPE html>
<html lang="en">
<head>
<meta charset="utf-8">
<title>Summit Floor Inspections – Business Cards</title>
<link href="https://fonts.googleapis.com/css2?family=Lato:wght@400;700;900&display=swap" rel="stylesheet">
<style>
  :root{
    --bg:#d3d4cf;
    --paper:#ffffff;
    --ink:#050505;
    --blue:#3a9ad9;
    --grey:#6f7174;
    --grey-light:#9a9c9f;
  }
  *{margin:0;padding:0;box-sizing:border-box}
  html,body{width:1200px;height:801px;overflow:hidden}
  body{background:var(--bg);font-family:"Lato",sans-serif;display:flex;align-items:center;justify-content:center;gap:56px}
  .card{width:540px;height:309px;position:relative;border-bottom:5px solid var(--blue);box-shadow:0 10px 24px rgba(0,0,0,.22)}
  .card--front{background:var(--paper)}
  .card--back{background:var(--ink)}

  .brand{display:flex;align-items:center;gap:12px}
  .brand__dot{width:34px;height:34px;border-radius:50%;background:var(--blue);flex:none}
  .brand__name{font-family:"Lato",sans-serif;font-weight:900;color:var(--blue);text-transform:uppercase;letter-spacing:.04em;line-height:1.05}

  .card--front .brand{position:absolute;left:34px;top:118px}
  .card--front .brand__name{font-size:22px;width:170px}

  .divider{position:absolute;left:262px;top:78px;width:2px;height:130px;background:var(--blue)}

  .contact{position:absolute;left:292px;top:54px}
  .contact__name{font-weight:900;font-size:25px;color:var(--blue);text-transform:uppercase;letter-spacing:.01em}
  .contact__role{font-size:14px;color:var(--grey);margin-top:2px}
  .contact__list{list-style:none;margin-top:22px}
  .contact__item{display:flex;align-items:center;gap:10px;font-size:14px;color:var(--grey);margin-bottom:9px}
  .contact__icon{width:15px;height:15px;flex:none}

  .tagline{position:absolute;font-size:14px;color:var(--grey);text-transform:uppercase;letter-spacing:.04em}
  .card--front .tagline{right:34px;bottom:30px}

  .card--back .brand{position:absolute;left:0;right:0;top:92px;justify-content:center}
  .card--back .brand__dot{width:44px;height:44px}
  .card--back .brand__name{font-size:30px}
  .card--back .tagline{left:0;right:0;bottom:46px;text-align:center;color:var(--grey-light);font-size:15px}
</style>
</head>
<body>
  <section class="card card--front">
    <div class="brand">
      <span class="brand__dot"></span>
      <span class="brand__name">Summit Floor Inspections</span>
    </div>
    <div class="divider"></div>
    <div class="contact">
      <h1 class="contact__name">Daniel Marlowe</h1>
      <p class="contact__role">Founder &amp; CEO</p>
      <ul class="contact__list">
        <li class="contact__item">
          <svg class="contact__icon" viewBox="0 0 16 16" aria-hidden="true"><path d="M4 1.5l2.5 3-1.5 1.5a8 8 0 0 0 5 5l1.5-1.5 3 2.5-1.5 2.5C7 14 2 9 1.5 3z" fill="var(--blue)"/></svg>
          555-014-2870
        </li>
        <li class="contact__item">
          <svg class="contact__icon" viewBox="0 0 16 16" aria-hidden="true"><rect x="1" y="3" width="14" height="10" fill="var(--blue)"/><path d="M1 3l7 6 7-6" fill="none" stroke="#fff" stroke-width="1.3"/></svg>
          daniel@summitfloorinspect.com
        </li>
        <li class="contact__item">
          <svg class="contact__icon" viewBox="0 0 16 16" aria-hidden="true"><circle cx="8" cy="8" r="7" fill="var(--blue)"/><path d="M1 8h14M8 1v14M3 4.5h10M3 11.5h10" stroke="#fff" stroke-width=".9" fill="none"/><ellipse cx="8" cy="8" rx="3.2" ry="7" fill="none" stroke="#fff" stroke-width=".9"/></svg>
          www.summitfloorinspect.com
        </li>
      </ul>
    </div>
    <p class="tagline">Analysis &amp; Consulting</p>
  </section>

  <section class="card card--back">
    <div class="brand">
      <span class="brand__dot"></span>
      <span class="brand__name">Summit Floor Inspections</span>
    </div>
    <p class="tagline">Certified Floor Covering Inspection &amp; Consulting</p>
  </section>
</body>
</html>
```